Optimization existing Business Card

I need a revision of the business card, incl. Logo Design. I am a freelancer and have my headquarters in Berlin. I develop business consulting solutions for banks, insurance and StartUp Companies. I want a simple design of the business card. The final design should professionalism and commitment and openness to communicate. I'm open minded in addition to optimizing the existing logo / business card as well on a new idea / proposal for the logo. Idea would be for example the logo of this page: http://varlow-strategic.consulting.

Target Market(s)

Consulting, Banking, Investment Banking

Industry/Entity Type

Business

Contact Information for Business Card

siehe Anhang (please take a look into the attachments, important)

Font styles to use
Sans Serif

Requirements
Must have
• Please look at my specifications exactly !! (Please see my specifications), CEO Founder not
Should not have
• No gradient !! (No overarching color gradient)

```html
<!DOCTYPE html>
<html lang="en">
<head>
<meta charset="utf-8">
<title>Varlow Consulting – Business Card</title>
<link rel="stylesheet" href="https://fonts.googleapis.com/css2?family=Open+Sans:wght@400;600;700&display=swap">
<style>
  :root {
    --backdrop: #5ecfbd;
    --card: #f4f4f2;
    --ink: #1e1e1e;
    --brand-blue: #1f4fd1;
    --card-shadow: rgba(20, 70, 60, 0.28);
  }
  * { margin: 0; padding: 0; box-sizing: border-box; }
  html, body {
    width: 1200px;
    height: 1200px;
    overflow: hidden;
    background: var(--backdrop);
    font-family: "Open Sans", Arial, sans-serif;
    color: var(--ink);
  }
  .sheet {
    width: 1200px;
    height: 1200px;
    display: flex;
    align-items: center;
    justify-content: center;
    gap: 90px;
  }
  .card {
    width: 400px;
    height: 620px;
    background: var(--card);
    box-shadow: 0 18px 40px var(--card-shadow);
    position: relative;
  }
  /* Front */
  .wordmark {
    position: absolute;
    top: 44px;
    left: 40px;
    display: flex;
    align-items: center;
    gap: 14px;
    font-weight: 700;
    font-size: 30px;
    line-height: 1;
    letter-spacing: 0.5px;
    text-transform: uppercase;
  }
  .wordmark-square {
    width: 22px;
    height: 22px;
    background: var(--brand-blue);
  }
  .holder {
    position: absolute;
    left: 40px;
    top: 380px;
  }
  .holder-name {
    font-weight: 700;
    font-size: 26px;
    line-height: 1.2;
  }
  .holder-role {
    font-weight: 700;
    font-size: 26px;
    line-height: 1.2;
  }
  .address {
    position: absolute;
    left: 40px;
    top: 490px;
    font-weight: 600;
    font-size: 18px;
    line-height: 1.3;
  }
  /* Back */
  .back-mark {
    position: absolute;
    top: 210px;
    left: 0;
    right: 0;
    display: flex;
    justify-content: center;
    align-items: center;
    gap: 12px;
    font-weight: 700;
    font-size: 24px;
    text-transform: uppercase;
    letter-spacing: 0.5px;
  }
  .contact-list {
    position: absolute;
    left: 40px;
    bottom: 48px;
    list-style: none;
    font-weight: 600;
    font-size: 16px;
    line-height: 1.45;
  }
  .contact-list li {
    display: flex;
    align-items: center;
    gap: 8px;
  }
  .contact-list svg { width: 13px; height: 13px; fill: var(--ink); flex: none; }
</style>
</head>
<body>
<main class="sheet">
  <section class="card card-front" aria-label="Card front">
    <div class="wordmark"><span class="wordmark-square"></span><span>Varlow Consulting</span></div>
    <div class="holder">
      <p class="holder-name">Jonas Varlow</p>
      <p class="holder-role">CEO</p>
    </div>
    <address class="address" style="font-style:normal">
      Lindenweg 48<br>10117 Berlin<br>Germany
    </address>
  </section>

  <section class="card card-back" aria-label="Card back">
    <div class="back-mark"><span class="wordmark-square"></span><span>Varlow Consulting</span></div>
    <ul class="contact-list">
      <li>
        <svg viewBox="0 0 16 16" aria-hidden="true"><path d="M3 1h3l1.5 4-2 1.2a9 9 0 0 0 4.3 4.3L11 8.5 15 10v3a2 2 0 0 1-2 2A12 12 0 0 1 1 3a2 2 0 0 1 2-2z"/></svg>
        +49 (0) 30 55501284
      </li>
      <li>
        <svg viewBox="0 0 16 16" aria-hidden="true"><path d="M4 0h8a1 1 0 0 1 1 1v14a1 1 0 0 1-1 1H4a1 1 0 0 1-1-1V1a1 1 0 0 1 1-1zm1 2v10h6V2zm3 11a1 1 0 1 0 0 2 1 1 0 0 0 0-2z"/></svg>
        +49 (0) 176 55503917
      </li>
      <li>
        <svg viewBox="0 0 16 16" aria-hidden="true"><path d="M1 3h14v10H1zm1 1.2V12h12V4.2L8 8.5z"/></svg>
        jonas@varlow-consulting.de
      </li>
    </ul>
  </section>
</main>
</body>
</html>
```